TALVERN CREST LIMITED CALENDAR 2018

We need an innovative calendar design for our company for 2018. to give a brief description of our company:
"Talvern Crest was founded in 2016 to provide a wide range of management consultancy and advisory services to small and medium-sized companies operating in consumer-driven sectors. With more than 300 years of cumulative investment and advisory experience among our sector-focused seasoned professionals, we advise management teams on an aggregate of $850m worth of investments operating in the healthcare, education, food and beverage and logistics sectors within the MENASEA region; the region of our expertise."
We want the design to include the following 12 countries for each month:
1. UAE 2. Saudi Arabia 3. Kuwait 4. Bahrain 5. Qatar 6. Oman 7. Jordan 8. Egypt 9. Singapore 10. Malaysia 11. Thailand 12. Indonesia
The description/design for each month must include each country's economic growth, Per Capita Income, GDP, etc. That is what we wish for the final design for each month to communicate as our company is in to a wide range of Investment management and Advisory Services
Target Market(s)
FINANCIAL SERVICES AND CONSULTING
Industry/Entity Type
Financial Service
Font styles to use
Colors
Designer to choose colors to be used in the design.
Look and feel

```html
<!DOCTYPE html>
<html lang="en">
<head>
<meta charset="utf-8">
<title>Talvern Crest Calendar 2018</title>
<link href="https://fonts.googleapis.com/css2?family=Montserrat:wght@400;600;700;800&display=swap" rel="stylesheet">
<style>
:root{
  --bg:#e9e4dc;
  --maroon:#7d1a2b;
  --gold:#d9ad55;
  --navy:#2a2f55;
  --ink:#4a3a3a;
  --panel:rgba(255,255,255,.94);
}
*{box-sizing:border-box;margin:0;padding:0}
html,body{width:1200px;height:1200px;overflow:hidden}
body{background:var(--bg);font-family:'Montserrat',sans-serif;position:relative}
.card{position:absolute;width:455px;height:352px;overflow:hidden;box-shadow:4px 6px 10px rgba(0,0,0,.35)}
.card--sa{left:121px;top:130px}
.card--qa{left:121px;top:506px}
.card--om{left:625px;top:242px}
.card--ae{left:625px;top:616px}
.photo{position:absolute;inset:0}
.photo--sa{background:linear-gradient(180deg,#d8cdea 0%,#c6b7dc 35%,#a596bf 55%,#8a7ea0 75%,#6f6888 100%)}
.photo--qa{background:linear-gradient(180deg,#6f9fd0 0%,#a9c7e4 40%,#c9d6de 52%,#6e7f8c 62%,#40b0b0 70%,#2fa4a3 85%,#5cbcbc 100%)}
.photo--om{background:linear-gradient(180deg,#9cbbe0 0%,#c7d6e8 25%,#8e8276 45%,#b59a73 62%,#d9b989 80%,#c9a678 100%)}
.photo--ae{background:linear-gradient(180deg,#b9cde2 0%,#d7dde2 30%,#8f97a6 55%,#5f6779 75%,#4a4f60 100%)}
.stats{position:absolute;left:18px;top:17px;display:flex;color:var(--navy)}
.stats__col{padding-right:10px}
.stats__col--main{border-right:1px solid var(--navy);width:68px;padding-bottom:6px}
.stats__col--side{padding-left:12px}
.stat{margin-bottom:9px}
.stat dt{font-size:7px;font-weight:700}
.stat dd{font-size:5.5px;font-weight:400;margin-top:3px}
.cal{position:absolute;left:280px;top:13px;width:158px;background:var(--panel);border-radius:8px;padding:6px 10px 8px;color:var(--ink)}
.cal h2{font-size:9px;font-weight:600;text-align:center;color:var(--navy);margin-bottom:3px}
.card--qa .cal h2{color:#2c6ca8}
.cal__grid{display:grid;grid-template-columns:repeat(7,1fr);text-align:center;font-size:6.5px;line-height:10.3px}
.cal__grid .dow{font-weight:700;color:var(--navy)}
.band{position:absolute;left:0;top:277px;width:100%;height:56px;background:var(--maroon);display:flex;align-items:center;justify-content:space-between;padding:0 18px 0 22px}
.brand{display:flex;align-items:center;gap:7px;color:var(--gold);font-size:15px;font-weight:600;letter-spacing:2px}
.brand__mark{width:10px;height:10px;background:var(--gold)}
.country{color:var(--gold);font-size:15px;font-weight:800;letter-spacing:.3px}
</style>
</head>
<body>

<section class="card card--sa">
  <div class="photo photo--sa" role="img" aria-label="Photo of the Riyadh skyline at dusk with a tall tower"></div>
  <div class="stats">
    <dl class="stats__col stats__col--main">
      <div class="stat"><dt>GDP</dt><dd>US$ 165.0 billion</dd></div>
      <div class="stat"><dt>GDP Growth</dt><dd>1.0%</dd></div>
      <div class="stat"><dt>GDP Per Capita</dt><dd>US$ 20,957.21</dd></div>
      <div class="stat"><dt>Population</dt><dd>32.6 million</dd></div>
    </dl>
    <dl class="stats__col stats__col--side">
      <div class="stat"><dt>Stock Market Cap</dt><dd>7,201.21</dd></div>
    </dl>
  </div>
  <div class="cal">
    <h2>September 2018</h2>
    <div class="cal__grid">
      <span class="dow">Sun</span><span class="dow">Mon</span><span class="dow">Tue</span><span class="dow">Wed</span><span class="dow">Thu</span><span class="dow">Fri</span><span class="dow">Sat</span>
      <span></span><span></span><span></span><span></span><span></span><span></span><span>1</span>
      <span>2</span><span>3</span><span>4</span><span>5</span><span>6</span><span>7</span><span>8</span>
      <span>9</span><span>10</span><span>11</span><span>12</span><span>13</span><span>14</span><span>15</span>
      <span>16</span><span>17</span><span>18</span><span>19</span><span>20</span><span>21</span><span>22</span>
      <span>23</span><span>24</span><span>25</span><span>26</span><span>27</span><span>28</span><span>29</span>
      <span>30</span>
    </div>
  </div>
  <div class="band">
    <div class="brand"><span class="brand__mark"></span>TALVERN CREST</div>
    <div class="country">SAUDI ARABIA</div>
  </div>
</section>

<section class="card card--qa">
  <div class="photo photo--qa" role="img" aria-label="Photo of the Doha skyline across turquoise bay water with boats"></div>
  <div class="stats">
    <dl class="stats__col stats__col--main">
      <div class="stat"><dt>GDP</dt><dd>US$ 152.5 billion</dd></div>
      <div class="stat"><dt>GDP Growth</dt><dd>0.6%</dd></div>
      <div class="stat"><dt>GDP Per Capita</dt><dd>US$ 58,246.65</dd></div>
      <div class="stat"><dt>Population</dt><dd>2.5 million</dd></div>
    </dl>
    <dl class="stats__col stats__col--side">
      <div class="stat"><dt>Stock Market Cap</dt><dd>8,500.08</dd></div>
    </dl>
  </div>
  <div class="cal">
    <h2>October 2018</h2>
    <div class="cal__grid">
      <span class="dow">Sun</span><span class="dow">Mon</span><span class="dow">Tue</span><span class="dow">Wed</span><span class="dow">Thu</span><span class="dow">Fri</span><span class="dow">Sat</span>
      <span></span><span>1</span><span>2</span><span>3</span><span>4</span><span>5</span><span>6</span>
      <span>7</span><span>8</span><span>9</span><span>10</span><span>11</span><span>12</span><span>13</span>
      <span>14</span><span>15</span><span>16</span><span>17</span><span>18</span><span>19</span><span>20</span>
      <span>21</span><span>22</span><span>23</span><span>24</span><span>25</span><span>26</span><span>27</span>
      <span>28</span><span>29</span><span>30</span><span>31</span>
    </div>
  </div>
  <div class="band">
    <div class="brand"><span class="brand__mark"></span>TALVERN CREST</div>
    <div class="country">QATAR</div>
  </div>
</section>

<section class="card card--om">
  <div class="photo photo--om" role="img" aria-label="Photo of a sandstone fort before rocky mountains in Oman"></div>
  <div class="stats">
    <dl class="stats__col stats__col--main">
      <div class="stat"><dt>GDP</dt><dd>US$ 17.1 billion</dd></div>
      <div class="stat"><dt>GDP Growth</dt><dd>11.71%</dd></div>
      <div class="stat"><dt>GDP Per Capita</dt><dd>US$ 16,790.6</dd></div>
      <div class="stat"><dt>Population</dt><dd>4.6 million</dd></div>
    </dl>
    <dl class="stats__col stats__col--side">
      <div class="stat"><dt>Stock Market Cap</dt><dd>5,040.430</dd></div>
    </dl>
  </div>
  <div class="cal">
    <h2>November 2018</h2>
    <div class="cal__grid">
      <span class="dow">Sun</span><span class="dow">Mon</span><span class="dow">Tue</span><span class="dow">Wed</span><span class="dow">Thu</span><span class="dow">Fri</span><span class="dow">Sat</span>
      <span></span><span></span><span></span><span></span><span>1</span><span>2</span><span>3</span>
      <span>4</span><span>5</span><span>6</span><span>7</span><span>8</span><span>9</span><span>10</span>
      <span>11</span><span>12</span><span>13</span><span>14</span><span>15</span><span>16</span><span>17</span>
      <span>18</span><span>19</span><span>20</span><span>21</span><span>22</span><span>23</span><span>24</span>
      <span>25</span><span>26</span><span>27</span><span>28</span><span>29</span><span>30</span>
    </div>
  </div>
  <div class="band">
    <div class="brand"><span class="brand__mark"></span>TALVERN CREST</div>
    <div class="country">OMAN</div>
  </div>
</section>

<section class="card card--ae">
  <div class="photo photo--ae" role="img" aria-label="Photo of the Dubai skyline and highway interchange"></div>
  <div class="stats">
    <dl class="stats__col stats__col--main">
      <div class="stat"><dt>GDP</dt><dd>US$ 407.52 billion</dd></div>
      <div class="stat"><dt>GDP Growth</dt><dd>2.7%</dd></div>
      <div class="stat"><dt>GDP Per Capita</dt><dd>US$ 40,162</dd></div>
      <div class="stat"><dt>Population</dt><dd>9.4 million</dd></div>
    </dl>
    <dl class="stats__col stats__col--side">
      <div class="stat"><dt>Stock Market Cap</dt><dd>4,369.40</dd></div>
    </dl>
  </div>
  <div class="cal">
    <h2>December 2018</h2>
    <div class="cal__grid">
      <span class="dow">Sun</span><span class="dow">Mon</span><span class="dow">Tue</span><span class="dow">Wed</span><span class="dow">Thu</span><span class="dow">Fri</span><span class="dow">Sat</span>
      <span></span><span></span><span></span><span></span><span></span><span></span><span>1</span>
      <span>2</span><span>3</span><span>4</span><span>5</span><span>6</span><span>7</span><span>8</span>
      <span>9</span><span>10</span><span>11</span><span>12</span><span>13</span><span>14</span><span>15</span>
      <span>16</span><span>17</span><span>18</span><span>19</span><span>20</span><span>21</span><span>22</span>
      <span>23</span><span>24</span><span>25</span><span>26</span><span>27</span><span>28</span><span>29</span>
      <span>30</span><span>31</span>
    </div>
  </div>
  <div class="band">
    <div class="brand"><span class="brand__mark"></span>TALVERN CREST</div>
    <div class="country">UNITED ARAB EMIRATES</div>
  </div>
</section>

</body>
</html>
```